RAmio Shop Business Card Design

My auto shop is targeted to the European and Asian luxury automotive market. We do mechanics collision and parts.
Some of the makes are KTR, DQ, Stone Herald, Valdine,Norvi, solavanta, bremo, HJ, etc. But in the end we get all makes.
I don't want to have the makes logos on the business card.
The Name of the business is after my first Name Ramiro but without the s Ramio Shop if there is any other ideas about the name iam open to suggestions. And i don't have a LOGO. Need logo!
Updates

Reason: I increased my budget and invited more designers. And committed payment so giving you guys more time.

Target Market(s)

target is the luxury auto market

Industry/Entity Type

Automotive

Contact Information for Business Card

European Automotive Repair Shop, Collision Mechanics Parts
Ramiro Villalba Owner, Colibrí #14 Loma Serena 2

Requirements
Nice to have
• One design i can of liked was the use of the dash error logos like check engine light airbag light. Nobla press has this but dose not include the air bag light. For the collision part of the business. But am open to any design.
Should not have
• exact logo makes on front of card.

```html
<!DOCTYPE html>
<html lang="en">
<head>
<meta charset="utf-8">
<title>Ramio Shop – Business Card</title>
<link rel="stylesheet" href="https://fonts.googleapis.com/css2?family=Cinzel:wght@400;500&family=Open+Sans:ital,wght@0,700;1,600&display=swap">
<style>
  :root {
    --card-black: #070707;
    --rule-red: #7a1414;
    --accent-red: #e0141b;
    --gold: #f2c23a;
    --white: #f4f4f4;
    --dash-violet: #8b7fd6;
    --dash-dark: #0d0d10;
    --dash-glow: #5a0b0b;
  }
  * { margin: 0; padding: 0; box-sizing: border-box; }
  html, body { width: 1200px; height: 702px; overflow: hidden; background: var(--card-black); }
  .card { position: relative; width: 1200px; height: 702px; background: var(--card-black); overflow: hidden; }
  .card__art { position: absolute; inset: 0; }
  .rule { position: absolute; left: 0; height: 2px; background: var(--rule-red); }
  .rule--1 { top: 387px; width: 660px; }
  .rule--2 { top: 456px; width: 700px; }
  .rule--3 { top: 594px; width: 770px; }
  .rule--4 { top: 641px; width: 800px; }
  .shop-name {
    position: absolute; left: 86px; top: 282px;
    font-family: "Cinzel", serif; font-weight: 400; font-size: 70px; line-height: 1;
    color: var(--white); letter-spacing: 3px; white-space: nowrap;
  }
  .tagline {
    position: absolute; left: 70px; top: 407px;
    font-family: "Open Sans", sans-serif; font-weight: 700; font-size: 29px;
    color: var(--gold); white-space: nowrap;
  }
  .owner { position: absolute; left: 74px; top: 488px; text-align: center; width: 368px; }
  .owner__name {
    font-family: "Cinzel", serif; font-style: italic; font-size: 40px; line-height: 1;
    color: var(--white); white-space: nowrap;
  }
  .owner__role {
    margin-top: 4px;
    font-family: "Cinzel", serif; font-size: 28px; line-height: 1; color: var(--gold);
  }
  .services { position: absolute; left: 458px; top: 470px; list-style: none; }
  .services li {
    display: flex; align-items: center; gap: 18px;
    font-family: "Open Sans", sans-serif; font-style: italic; font-weight: 600;
    font-size: 35px; line-height: 38px; color: var(--white);
  }
  .services li::before {
    content: ""; width: 18px; height: 6px; background: var(--dash-violet);
    transform: skewX(-20deg); border-radius: 2px;
  }
  .address {
    position: absolute; left: 120px; top: 604px;
    font-family: "Cinzel", serif; font-size: 29px; line-height: 1;
    color: var(--white); letter-spacing: 1px; white-space: nowrap;
  }
</style>
</head>
<body>
<div class="card">
  <svg class="card__art" width="1200" height="702" viewBox="0 0 1200 702">
    <defs>
      <radialGradient id="dashGlow" cx="0.55" cy="0.5" r="0.7">
        <stop offset="0" stop-color="#1b1b20"/>
        <stop offset="0.6" stop-color="var(--dash-dark)"/>
        <stop offset="1" stop-color="var(--dash-glow)"/>
      </radialGradient>
    </defs>
    <polygon points="386,0 1200,0 1200,702 836,702" fill="url(#dashGlow)" role="img"
      aria-label="Close-up photo of a car instrument cluster: tachometer dial with needle and glowing dashboard warning lights"/>
    <line x1="386" y1="0" x2="836" y2="702" stroke="var(--accent-red)" stroke-width="7"/>
  </svg>

  <div class="rule rule--1"></div>
  <div class="rule rule--2"></div>
  <div class="rule rule--3"></div>
  <div class="rule rule--4"></div>

  <h1 class="shop-name">Ramio Shop</h1>
  <p class="tagline">European Automotive Repair Shop</p>

  <div class="owner">
    <p class="owner__name">Ramiro Villalba</p>
    <p class="owner__role">Owner</p>
  </div>

  <ul class="services">
    <li>Collisions</li>
    <li>Mechanics</li>
    <li>Parts</li>
  </ul>

  <p class="address">Colibrí #14 Loma Serena 2</p>
</div>
</body>
</html>
```